Velquor Web Site

We need a new web site for a new company, Velquor Pty Ltd.
The company will provide services around the Brintara Skyhold and Tallowbench Suite products.
The company theme is "Work is what you do, not where you go." We aim to separate the concepts of data and place. Our clients can access their data anywhere, any time.
The design should look modern, international and should include the Brintara Associate logo.
Updates
My existing web site is visible at http://quennelworks.example. I am hoping that a good designer can provide a fresh look for the business.
Three images for "Cloud" uploaded today.
Target Market(s)
Business of all kinds
Industry/Entity Type
It Company
Requirements
Nice to have
- Colors and themes might reflect Brintara look and style.

```html
<!DOCTYPE html>
<html lang="en">
<head>
<meta charset="utf-8">
<title>Velquor</title>
<link rel="stylesheet" href="https://fonts.googleapis.com/css2?family=Source+Sans+3:wght@300;400;600&family=Arimo:wght@400&display=swap">
<style>
:root{
  --navy:#0b3461;
  --navy-text:#0f3a66;
  --link:#1a7fd0;
  --ink:#444;
  --topbar:#4a4a4a;
  --topbar-active:#2c2c2c;
  --footer:#4b4b4b;
  --footer-base:#3a3a3a;
  --footer-text:#e6e6e6;
  --white:#fff;
}
*{margin:0;padding:0;box-sizing:border-box}
html,body{width:1200px;height:888px;overflow:hidden;background:var(--white)}
body{font-family:"Source Sans 3",sans-serif;color:var(--ink);position:relative}
a{text-decoration:none;color:inherit}

.top-nav{height:27px;background:var(--topbar);display:flex;justify-content:flex-end;padding-right:0}
.top-nav a{font-family:Arimo,sans-serif;font-size:12px;color:#ddd;padding:0 13px;line-height:27px}
.top-nav a.active{background:var(--topbar-active);color:var(--white);margin-right:0}
.top-nav ul{display:flex;list-style:none;margin-right:119px}

.wrap{width:942px;margin-left:129px;position:relative}

.site-header{height:102px;display:flex;justify-content:space-between;align-items:center}
.brand{display:flex;align-items:center;gap:10px;color:var(--navy-text);font-weight:600;font-size:31px;margin-top:4px}
.brand-mark{width:20px;height:20px;border-radius:50%;background:var(--navy)}
.header-contact{text-align:right;color:var(--navy-text);font-size:18px;line-height:23px;margin-top:6px}

.hero{height:368px;display:flex}
.hero-photo{width:605px;height:100%;position:relative;background:linear-gradient(160deg,#5d7995 0%,#a9bccd 35%,#d7dde3 55%,#6f7f8a 100%)}
.hero-caption{position:absolute;left:0;right:0;bottom:0;height:49px;background:rgba(0,0,0,.72);color:var(--white);font-weight:300;font-size:29px;line-height:49px;padding-left:10px;letter-spacing:-.3px}
.hero-panel{flex:1;background:var(--navy);color:var(--white);padding:82px 0 0 25px}
.hero-panel h2{font-weight:300;font-size:30px;margin-bottom:10px}
.tick-list{list-style:none}
.tick-list li{display:flex;align-items:center;gap:9px;font-weight:300;font-size:16px;line-height:25.7px}
.tick-list svg{width:14px;height:12px;flex:none}

.features{height:179px;position:relative}
.feature{position:absolute;top:0}
.feature h3{font-weight:400;font-size:19px;color:var(--navy-text);line-height:22px}
.feature p{font-size:13px;line-height:17px;color:var(--ink);margin-top:8px}
.feature .more{display:block;color:var(--link);font-size:14.5px;margin-top:7px}
.f-partner{left:0;top:40px;width:215px}
.partner-badge{margin-top:8px;position:relative;height:60px}
.partner-badge .badge-shape{position:absolute;left:140px;top:0;width:34px;height:34px;background:#6cb8a8;border-radius:4px}
.partner-badge .badge-name{position:absolute;left:2px;top:34px;font-size:19px;color:#222;font-weight:400}
.f-customers{left:279px;top:50px}
.customer-name{margin-top:14px;font-size:22px;font-weight:600;color:#f2a81d;line-height:24px}
.f-cloud{left:477px;top:48px;width:230px}
.f-sky{left:746px;top:48px;width:200px}

.site-footer{position:absolute;left:0;top:676px;width:1200px;height:181px;background:var(--footer);color:var(--footer-text)}
.site-footer .wrap{height:100%}
.testimonials{position:absolute;left:0;top:26px;width:680px}
.testimonials h2,.contact h2{font-weight:300;font-size:25px;color:var(--white)}
.contact h2{font-size:19px;font-weight:400}
.quote-block{display:flex;margin-top:12px}
.quote-org{width:160px;height:54px;background:#3f6fa8;color:var(--white);font-size:20px;display:flex;align-items:center;justify-content:center;flex:none;margin-left:1px}
.quote-text{margin-left:32px;font-size:13.5px;line-height:20.5px;width:480px}
.quote-author{font-weight:600;font-size:13.5px;margin-top:13px;margin-left:2px}
.contact{position:absolute;left:739px;top:28px;font-size:12.5px;line-height:17px}
.contact address{font-style:normal;margin-top:14px}
.contact strong{font-weight:600}

.footer-base{position:absolute;left:0;top:857px;width:1200px;height:31px;background:var(--footer-base);color:#ccc;font-size:11.5px}
.footer-base .wrap{display:flex;justify-content:space-between;line-height:31px;padding:0 2px}
.footer-links{display:flex;gap:8px;font-size:12px}
</style>
</head>
<body>
<nav class="top-nav">
  <ul><li><a class="active" href="#">Home</a></li><li><a href="#">Cloud Services</a></li></ul>
</nav>

<div class="wrap">
  <header class="site-header">
    <a class="brand" href="#"><span class="brand-mark"></span>Velquor</a>
    <div class="header-contact">08 5550 1427<br>service@velquor.example</div>
  </header>

  <section class="hero">
    <div class="hero-photo" role="img" aria-label="Photo of two business people looking at a laptop in front of city towers">
      <div class="hero-caption">Work is what you do, not where you go.</div>
    </div>
    <div class="hero-panel">
      <h2>Safe and Secure</h2>
      <ul class="tick-list">
        <li><svg viewBox="0 0 14 12"><path d="M1 6.5l4 4L13 1.5" fill="none" stroke="#fff" stroke-width="2.6"/></svg>Work is what you do, not where you do it</li>
        <li><svg viewBox="0 0 14 12"><path d="M1 6.5l4 4L13 1.5" fill="none" stroke="#fff" stroke-width="2.6"/></svg>Access your files, anywhere, any time</li>
        <li><svg viewBox="0 0 14 12"><path d="M1 6.5l4 4L13 1.5" fill="none" stroke="#fff" stroke-width="2.6"/></svg>Use the best skills, where ever they are</li>
        <li><svg viewBox="0 0 14 12"><path d="M1 6.5l4 4L13 1.5" fill="none" stroke="#fff" stroke-width="2.6"/></svg>Activate Brintara's Skyhold services</li>
        <li><svg viewBox="0 0 14 12"><path d="M1 6.5l4 4L13 1.5" fill="none" stroke="#fff" stroke-width="2.6"/></svg>Tallowbench Suite is anywhere you want it to be</li>
        <li><svg viewBox="0 0 14 12"><path d="M1 6.5l4 4L13 1.5" fill="none" stroke="#fff" stroke-width="2.6"/></svg>Available around the clock</li>
      </ul>
    </div>
  </section>

  <section class="features">
    <div class="feature f-partner">
      <h3>We are proudly parterner of Brintara</h3>
      <div class="partner-badge">
        <span class="badge-shape"></span>
        <span class="badge-name">Brintara Associate</span>
      </div>
    </div>
    <div class="feature f-customers">
      <h3>Our Customers</h3>
      <div class="customer-name">Harrowfin Marine</div>
    </div>
    <div class="feature f-cloud">
      <h3>Cloud Data Anywhere</h3>
      <p>We help your business and your people work anywhere, any time</p>
      <a class="more" href="#">Read More</a>
    </div>
    <div class="feature f-sky">
      <h3>Brintara Skyhold</h3>
      <p>World wide data at your fingertips</p>
      <a class="more" href="#">Read More</a>
    </div>
  </section>
</div>

<footer class="site-footer">
  <div class="wrap">
    <section class="testimonials">
      <h2>Testimonials</h2>
      <div class="quote-block">
        <div class="quote-org">Tesslon</div>
        <p class="quote-text">"You are a legend. We have an audit in progress today and I was able to illustrate a "Live" recovery. Thank you for service above and beyond the call of duty. We really appreciate that."</p>
      </div>
      <p class="quote-author">Martin Oakes, Tesslon Planning</p>
    </section>
    <section class="contact">
      <h2>Contact Us</h2>
      <address>
        PO Box 412, Carrow Bay<br>
        Western Region, 6900<br>
        <strong>Telephone:</strong>&nbsp; 08 5550 1427<br>
        <strong>Email Information and Support:</strong><br>
        service@velquor.example
      </address>
    </section>
  </div>
</footer>

<div class="footer-base">
  <div class="wrap">
    <span>Copyright © 2013 Velquor. All Rights Reserved.</span>
    <span class="footer-links"><a href="#">Home</a><span>•</span><a href="#">Cloud Services</a></span>
  </div>
</div>
</body>
</html>
```